Corporate PowerPoint design for edtech focused on developing world / emerging markets

I am involved in a edtech startup focused on providing financial literacy for students and young adults in the developing world and emerging markets; currently focus will be on Africa. We are in discussions with the CEO of a bank in S. Africa and would deploy products throughout much of Africa with them. I need a corporate powerpoint that I can use for my customers and for investor presentation. Company name is Tidemark, which is a surfing term; meant to connotate movement and energy.

Reason: meeting with my partners to evaluate designs later this week.

Target Market(s)

target market is two fold - will be selling to execs at banks and telecommunications companies; also need to present to investors.

Industry/Entity Type

Financial

Font styles to use
Sans Serif

Requirements
Must have
• I'd like to have a slide or two that allow me to do columns for things like feature / benefits or just content that doesn't run left to right across the entire powepoint page.
• otherwise, too much color (other than white) uses a ton of ink, so I don't want a full color background e.g. I don't want a blue or green background. I would like to provide some standard corporate info at the bottom - just basics of contact info, url and ability to change them as necessary

```html
<!DOCTYPE html>
<html lang="en">
<head>
<meta charset="utf-8">
<title>Tidemark – Presentation Slides</title>
<link href="https://fonts.googleapis.com/css2?family=Carlito:wght@400;700&family=Open+Sans:wght@400;600;700&display=swap" rel="stylesheet">
<style>
  :root {
    --stage: #5e5e60;
    --paper: #ffffff;
    --teal: #1fa39b;
    --teal-dark: #137a74;
    --blue: #1570b8;
    --blue-dark: #0d4d80;
    --ink: #111111;
    --rule: #9a9a9a;
    --grid: #c9c9c9;
    --label: #333333;
  }
  * { margin: 0; padding: 0; box-sizing: border-box; }
  html, body { width: 1200px; height: 848px; overflow: hidden; background: var(--stage); }
  body { position: relative; font-family: "Carlito", "Calibri", sans-serif; color: var(--ink); }

  .slide { position: absolute; background: var(--paper); overflow: hidden; }
  .slide--chart { left: 34px; top: 27px; width: 536px; height: 401px; }
  .slide--benefits { left: 625px; top: 27px; width: 536px; height: 401px; }
  .slide--closing { left: 364px; top: 447px; width: 490px; height: 366px; }

  .slide__title {
    position: absolute; left: 59px; top: 40px;
    font-family: "Open Sans", sans-serif; font-size: 14.5px; font-weight: 400; letter-spacing: 0.2px;
  }
  .slide__title em { font-style: normal; font-weight: 700; color: var(--teal); }

  .body-copy { position: absolute; font-size: 11px; line-height: 14.5px; text-align: center; }
  .slide--chart .body-copy { left: 60px; top: 283px; width: 416px; }
  .slide--benefits .body-copy { left: 50px; top: 73px; width: 420px; }

  .chart { position: absolute; left: 38px; top: 96px; }

  .legend { position: absolute; left: 308px; width: 200px; font-size: 9.5px; line-height: 12.5px; }
  .legend__swatch { position: absolute; left: 0; top: 1px; width: 11px; height: 11px; }
  .legend__head { margin-left: 18px; font-size: 11px; font-weight: 700; margin-bottom: 1px; }
  .legend__text { margin-left: 19px; }
  .legend__text span { display: block; padding-left: 13px; }
  .legend--a { top: 109px; }
  .legend--b { top: 180px; }
  .legend--a .legend__swatch { background: var(--teal); }
  .legend--b .legend__swatch { background: var(--blue); }

  .footer__brand {
    position: absolute; left: 17px; top: 352px; display: flex; align-items: center; gap: 4px;
    font-family: "Carlito", sans-serif; font-weight: 700; font-size: 19px; letter-spacing: 0.3px; color: var(--teal);
  }
  .footer__dot { width: 13px; height: 13px; border-radius: 50%; background: var(--teal); }
  .footer__rule { position: absolute; left: 171px; right: 0; top: 365px; border-top: 1px solid var(--rule); }
  .footer__page { position: absolute; right: 18px; top: 376px; font-size: 12px; }

  .column { position: absolute; top: 169px; width: 179px; height: 148px; }
  .column--left { left: 58px; }
  .column--right { left: 304px; }
  .column__box { position: absolute; left: 9px; top: 0; right: 0; bottom: 0; border: 1.3px solid var(--ink); }
  .column__tab {
    position: absolute; left: 0; top: 0; right: 0; height: 22px;
    color: #fff; font-size: 12px; font-weight: 700; line-height: 22px; text-align: center;
  }
  .column__fold { position: absolute; left: 0; top: 22px; width: 0; height: 0; border-left: 9px solid transparent; }
  .column--left .column__tab { background: var(--teal); }
  .column--left .column__fold { border-top: 7px solid var(--teal-dark); }
  .column--right .column__tab { background: var(--blue); }
  .column--right .column__fold { border-top: 7px solid var(--blue-dark); }
  .column__list { position: absolute; left: 15px; top: 30px; list-style: none; font-size: 9.5px; }
  .column__list li { height: 25px; position: relative; padding-left: 9px; }
  .column__list li::before { content: ""; position: absolute; left: 0; top: 4px; width: 3.5px; height: 3.5px; background: var(--ink); }

  .closing__title { position: absolute; left: 0; right: 0; top: 94px; text-align: center; font-family: "Open Sans", sans-serif; font-weight: 700; font-size: 15px; }
  .closing__brand {
    position: absolute; left: 0; right: 0; top: 132px; display: flex; justify-content: center; align-items: center; gap: 6px;
    font-weight: 700; font-size: 26px; letter-spacing: 0.4px; color: var(--teal);
  }
  .closing__dot { width: 19px; height: 19px; border-radius: 50%; background: var(--teal); }
  .contact { position: absolute; left: 0; right: 0; top: 182px; text-align: center; font-size: 10.5px; line-height: 13px; font-style: normal; }
  .contact__head { font-weight: 700; }
  .closing__url { position: absolute; left: 0; right: 0; top: 337px; text-align: center; font-size: 11px; }
</style>
</head>
<body>

<section class="slide slide--chart">
  <h2 class="slide__title">YOUR CHART <em>COMES HERE</em></h2>

  <svg class="chart" width="262" height="160" viewBox="0 0 262 160" role="img" aria-label="Bar chart comparing two series across four categories">
    <g stroke="var(--grid)" stroke-width="1">
      <line x1="3" y1="2" x2="220" y2="2"/>
      <line x1="3" y1="29" x2="220" y2="29"/>
      <line x1="3" y1="56" x2="220" y2="56"/>
      <line x1="3" y1="83" x2="220" y2="83"/>
      <line x1="3" y1="109" x2="220" y2="109"/>
      <line x1="3" y1="136" x2="220" y2="136"/>
    </g>
    <g fill="var(--teal)">
      <rect x="14" y="20" width="16" height="116"/>
      <rect x="69" y="69" width="15" height="67"/>
      <rect x="123" y="42" width="16" height="94"/>
      <rect x="177" y="15" width="16" height="121"/>
    </g>
    <g fill="var(--blue)">
      <rect x="30" y="72" width="16" height="64"/>
      <rect x="84" y="17" width="16" height="119"/>
      <rect x="139" y="88" width="16" height="48"/>
      <rect x="193" y="61" width="16" height="75"/>
    </g>
    <g font-family="Carlito, sans-serif" font-size="8.5" fill="var(--label)" text-anchor="middle">
      <text x="30" y="154">Category 1</text>
      <text x="84" y="154">Category 2</text>
      <text x="139" y="154">Category 3</text>
      <text x="193" y="154">Category 4</text>
    </g>
  </svg>

  <div class="legend legend--a">
    <span class="legend__swatch"></span>
    <p class="legend__head">Ask the basic questions:-</p>
    <p class="legend__text"><span>As you define and allocate</span>tasks&nbsp; as You want in it this is the</p>
  </div>
  <div class="legend legend--b">
    <span class="legend__swatch"></span>
    <p class="legend__head">Ask the basic questions:-</p>
    <p class="legend__text"><span>As you define and allocate</span>tasks&nbsp; as You want in it this is the</p>
  </div>

  <p class="body-copy">Ask the basic questions as you define and allocate tasks (workload/complexity, dependencies, time to complete, fit with capabilities). Make sure the workload is balanced and allocated fairly&nbsp; Ask the basic questions as you define and allocate tasks</p>

  <div class="footer__brand">TIDEMARK <span class="footer__dot"></span></div>
  <div class="footer__rule"></div>
  <span class="footer__page">03</span>
</section>

<section class="slide slide--benefits">
  <h2 class="slide__title">BENEFITS OF <em>THE COMPANY</em></h2>

  <p class="body-copy">Ask the basic questions as you define and allocate tasks (workload/complexity, dependencies, time to complete, fit with capabilities). Make sure the workload is balanced and allocated fairly&nbsp; Ask the basic questions as you define and allocate tasks</p>

  <div class="column column--left">
    <div class="column__box"></div>
    <div class="column__tab">Ask the basic questions:-</div>
    <span class="column__fold"></span>
    <ul class="column__list">
      <li>Insert your one by one points here</li>
      <li>Insert your one by one points here</li>
      <li>Insert your one by one points here</li>
      <li>Insert your one by one points here</li>
    </ul>
  </div>

  <div class="column column--right">
    <div class="column__box"></div>
    <div class="column__tab">Ask the basic questions:-</div>
    <span class="column__fold"></span>
    <ul class="column__list">
      <li>Insert your one by one points here</li>
      <li>Insert your one by one points here</li>
      <li>Insert your one by one points here</li>
      <li>Insert your one by one points here</li>
    </ul>
  </div>

  <div class="footer__brand">TIDEMARK <span class="footer__dot"></span></div>
  <div class="footer__rule"></div>
  <span class="footer__page">04</span>
</section>

<section class="slide slide--closing">
  <h2 class="closing__title">THANK YOU</h2>
  <div class="closing__brand">TIDEMARK <span class="closing__dot"></span></div>
  <address class="contact">
    <p class="contact__head">Contact details:</p>
    <p>Office phone : 0215550147</p>
    <p>Mobile : 0825550193</p>
    <p>fax no: 021-555018</p>
  </address>
  <p class="closing__url">www.tidemark-learn.com</p>
</section>

</body>
</html>
```